Landing Page für B2B-Softwareentwicklungsfirma
Zielgruppe
Wir sind eine (relativ kleine) B2B Softwareentwicklungsfirma, die Software zum Wetten auf Pferderennen erstellt.
Unsere Kunden sind Buchmacher und Rennbahnbetreiber.
Unsere Software läuft auf verschiedener Hardware (Touchscreen Terminals, Handy, Kassa, Webseite,...) und wird teilweise von Endkunden (Sportwetter) als auch Kunden-Mitarbeitern verwendet.
Was uns von anderen Softwarefirmen in diesem Bereich unterscheidet ist:
- Wir sind extrem verlässlich und unsere Software läuft störungsfrei
- Wir haben extrem viel Knowhow und ein großes Netzwerk im Bereich Pferdesport/-wetten
- Wir sind flexibel, gehen auf Kundenwünsche immer schnell und kosteneffizient ein
- Unsere softwaretechnischen Fähigkeiten sind ausgezeichnet (wir sind hauptsächlich Programmierer - weniger Businessleute).
- Wir sind für unsere Kunden immer persönlich, direkt und einfach ansprechbar (kleine Firma)
- Wir sind seit ca 15 Jahren erfolgreich im Markt, und auch Marktführer im deutschsprachigen Raum
- Wir haben ein sehr breites Produktportfolio (Terminal, Kassa, Mobile Webseite, Desktop Webseite, Backoffice, Risk Management)
- Wir legen viel Wert auf sauberes und auch modernes UI/UX-Design
Wir benötigen nun einen professionellen Webauftritt um in neue Märkte einzutreten.
Als ersten Schritt möchten wir gerne eine Single-Page Landingpage, die alle wichtigen Punkte im Überblick darstellt.
Aufgabenstellung
Das Design soll die Punkte aus der obigen Beschreibung über uns widerspiegeln, und auch unsere Werte:
Wichtig: Modern, Verlässlichkeit, Dynamisch, Kosteneffizient, Freundlich
Optional: Kreativ, Flexibilität
Wichtig ist auch der Bezug zum Pferderennsport!
Und dass wir eine B2B Softwarefirma sind!
Bitte beachten Sie unser neues Firmenlogo - siehe Anhang.
Die Landingpage soll eher hell, klar, offen, freundlich, sachlich sein.
Die Landingpage soll auf Mobile und Desktop funktionieren und gut aussehen.
Bitte verwenden Sie folgende Gliederung der Landingpage:
Sections:
....* Above the fold
........headline: horse betting software
........subheadline: Multi-product betting solution for bookmakers and racetrack operators.
................................Software production for land-based operations and online betting.
........call-to-action: get in touch
........secondary call-to-action: view products
........switch language
........links to other sections
....* Products
........Point of Sale
............Title: Quick and streamlined bet placement
............Short desc: Optimized bet placement solution for your bet shops and race tracks. Supports Windows-based touchscreen terminals and many different printers and scanners out of the box.
........Self-Service Terminals
............Title: Let users take control
............Short desc: Easy to use touchscreen software for new and professional punters. Running on any Windows-based hardware and adapted to your special needs.
........Web and Mobile Betting
............Title: Reach your target audience wherever they are
............Short desc: Allow your customers to enter their bets on any desktop or mobile browser.
........Bet Management
............Title: Stay in control of your meetings and bets
............Short desc: Browser-based Back-Office solution to control all your meetings,..

```html
<!DOCTYPE html>
<html lang="en">
<head>
<meta charset="utf-8">
<title>brightmoor – Horse Betting Software</title>
<link href="https://fonts.googleapis.com/css2?family=Poppins:wght@400;500;600;700&display=swap" rel="stylesheet">
<style>
:root{
  --ink:#1f2a3d;
  --text:#2c3444;
  --muted:#8a93a3;
  --accent:#3bc8ea;
  --primary:#0c5a8b;
  --hero-bg:#f4f4f6;
  --page-bg:#fafafb;
  --card:#ffffff;
  --line:#e8eaef;
  --blue:#3b5be0;
  --pink:#ea3a6d;
  --amber:#f4b13a;
  --teal:#3ed0a4;
  --green:#3ccf8e;
}
*{box-sizing:border-box;margin:0;padding:0}
html,body{width:1200px;height:2232px;overflow:hidden}
body{font-family:'Poppins',sans-serif;background:var(--page-bg);color:var(--text);position:relative}
.abs{position:absolute}
.hero{position:absolute;left:0;top:0;width:1200px;height:774px;background:var(--hero-bg)}
.brand{left:106px;top:38px;font-size:24px;font-weight:600;color:var(--ink);letter-spacing:1px;display:flex;align-items:center;gap:8px}
.brand .dot{width:12px;height:12px;border-radius:50%;background:var(--accent)}
.nav a{position:absolute;top:44px;font-size:14px;color:var(--ink);text-decoration:none}
.lang{left:920px;top:44px;font-size:14px;color:var(--ink)}
.btn{position:absolute;display:flex;align-items:center;justify-content:center;background:var(--primary);color:#fff;font-size:14.5px;font-weight:500;border-radius:4px;box-shadow:0 4px 8px rgba(12,90,139,.25);text-decoration:none}
.eyebrow{font-size:15px;font-weight:600;letter-spacing:1.5px;color:var(--accent);text-transform:uppercase}
.hero-title{left:97px;top:224px;font-size:49px;font-weight:700;line-height:58px;color:var(--ink)}
.hero-copy{left:97px;top:421px;width:420px;font-size:15.6px;line-height:27.5px;color:var(--text)}
.link{left:310px;top:584px;font-size:14.5px;color:var(--primary);font-weight:500;text-decoration:underline}
.card{position:absolute;background:var(--card);border-radius:14px;box-shadow:0 10px 30px rgba(30,40,70,.08)}
.section-head{left:0;width:1250px;text-align:center}
.products-title{top:910px;font-size:43px;font-weight:700;color:var(--ink)}
.products-copy{top:983px;font-size:16px;line-height:26px;color:var(--text)}
.prod-title{font-size:29px;font-weight:700;color:var(--ink)}
.prod-copy{font-size:15.6px;line-height:26px;width:500px}
.feature{position:absolute;width:146px;height:113px;background:#fff;border-radius:6px;box-shadow:0 3px 8px rgba(0,0,0,.12);display:flex;flex-direction:column;align-items:center;justify-content:flex-end;padding-bottom:18px;font-size:15.5px;color:var(--text)}
.feature.soft{background:#f6f6f8;box-shadow:none}
.feature svg{margin-bottom:10px}
.panel{position:absolute;background:#fff;border:1px solid var(--line);border-radius:8px}
.panel h4{font-size:13px;font-weight:600;color:var(--ink)}
.small{font-size:10px;color:var(--muted)}
</style>
</head>
<body>

<section class="hero">
  <div class="abs brand"><span class="dot"></span>brightmoor</div>
  <nav class="nav">
    <a style="left:397px">Products &#8964;</a>
    <a style="left:492px">Why us?</a>
    <a style="left:584px">Company &amp; Team</a>
    <a style="left:743px">FAQ</a>
  </nav>
  <div class="abs lang">DE / EN</div>
  <a class="btn" style="left:1008px;top:32px;width:90px;height:41px;box-shadow:none">Contact</a>

  <div class="abs eyebrow" style="left:97px;top:188px">Horse betting software providers</div>
  <h1 class="abs hero-title">The Reliable Way<br>To Manage<br>Your Horse Races</h1>
  <p class="abs hero-copy">We provide multi-product betting solutions for bookmakers and racetrack operators.<br>Our proven software products are a perfect fit for land-based as well as online betting operations.</p>
  <a class="btn" style="left:97px;top:569px;width:181px;height:48px">View our products</a>
  <a class="abs link">Get in touch</a>

  <div class="abs" style="left:617px;top:230px;width:377px;height:350px;border-radius:50%;background:var(--accent)"></div>
  <div class="abs" role="img" aria-label="Photo of a jockey riding a galloping racehorse" style="left:592px;top:240px;width:505px;height:360px;border-radius:48% 40% 45% 50%;background:linear-gradient(135deg,#6b3a24,#3b1f14 70%);opacity:.9"></div>

  <div class="card" style="left:938px;top:149px;width:151px;height:206px;padding:18px 16px">
    <div style="font-size:12px;font-weight:600;color:var(--ink)">Total Projects</div>
    <div style="font-size:21px;color:var(--ink);margin-top:12px">38</div>
    <div class="small" style="font-size:9px">Views</div>
    <svg width="120" height="50" style="margin-top:14px">
      <g stroke-width="3" stroke-linecap="round">
        <line x1="4" y1="48" x2="4" y2="28" stroke="#3b5be0"/><line x1="12" y1="48" x2="12" y2="36" stroke="#d8ddf5"/>
        <line x1="22" y1="48" x2="22" y2="20" stroke="#3b5be0"/><line x1="30" y1="48" x2="30" y2="32" stroke="#d8ddf5"/>
        <line x1="40" y1="48" x2="40" y2="14" stroke="#3b5be0"/><line x1="48" y1="48" x2="48" y2="8" stroke="#d8ddf5"/>
        <line x1="58" y1="48" x2="58" y2="30" stroke="#3b5be0"/><line x1="66" y1="48" x2="66" y2="22" stroke="#d8ddf5"/>
        <line x1="76" y1="48" x2="76" y2="18" stroke="#3b5be0"/><line x1="84" y1="48" x2="84" y2="34" stroke="#d8ddf5"/>
        <line x1="94" y1="48" x2="94" y2="38" stroke="#3b5be0"/><line x1="102" y1="48" x2="102" y2="26" stroke="#3b5be0"/>
        <line x1="112" y1="48" x2="112" y2="30" stroke="#d8ddf5"/>
      </g>
    </svg>
    <div style="font-size:8px;color:var(--ink);margin-top:10px;display:flex;align-items:center;gap:6px"><span style="width:18px;height:18px;border-radius:3px;background:#eef1fd;display:inline-block"></span>Projects Management</div>
  </div>

  <div class="card" style="left:843px;top:516px;width:225px;height:168px;padding:16px 18px">
    <div style="font-size:13px;font-weight:500;color:var(--ink)">Growth</div>
    <svg width="195" height="90" viewBox="0 0 195 90" style="position:absolute;left:17px;top:20px">
      <defs><linearGradient id="gfill" x1="0" y1="0" x2="0" y2="1"><stop offset="0" stop-color="#c9d2fb"/><stop offset="1" stop-color="#fff" stop-opacity="0"/></linearGradient></defs>
      <path d="M2 80 C20 50,32 58,45 64 C58 70,62 50,80 36 C96 26,110 44,128 20 C140 12,150 40,175 6 L175 70 L2 80Z" fill="url(#gfill)" opacity=".6"/>
      <path d="M2 80 C20 50,32 58,45 64 C58 70,62 50,80 36 C96 26,110 44,128 20 C140 12,150 40,175 6" fill="none" stroke="#3b5be0" stroke-width="2"/>
      <circle cx="57" cy="59" r="3" fill="#3b5be0" stroke="#fff"/>
      <circle cx="127" cy="21" r="3" fill="#f4c53a" stroke="#fff"/>
    </svg>
    <svg width="190" height="10" style="position:absolute;left:17px;top:122px">
      <circle cx="44" cy="5" r="4" fill="#f4c53a"/><rect x="52" y="3" width="50" height="4" rx="2" fill="#eceef3"/>
      <circle cx="122" cy="5" r="4" fill="#3b5be0"/><rect x="130" y="3" width="50" height="4" rx="2" fill="#d8ddea"/>
    </svg>
    <div class="small" style="position:absolute;left:17px;top:140px;width:200px;display:flex;justify-content:space-between;font-size:9px;color:#b2b8c4"><span>67</span><span>73</span><span>53</span><span>47</span><span>39</span><span>27</span><span>27</span></div>
  </div>
</section>

<div class="abs eyebrow section-head" style="top:876px">Betting solutions</div>
<h2 class="abs section-head products-title">Our Products</h2>
<p class="abs section-head products-copy">Neque egestas congue quisque egestas diam in. Semper quis<br>lectus nulla at volutpat diam ut venenatis.</p>

<!-- Point of Sale -->
<svg class="abs" style="left:98px;top:1152px" width="42" height="26"><path d="M2 6 L40 2 L24 12 L14 24 Z" fill="var(--accent)"/></svg>
<h3 class="abs prod-title" style="left:98px;top:1184px">Point of Sale</h3>
<p class="abs prod-copy" style="left:98px;top:1244px">Lorem ipsum dolor sit amet, consectetur adipiscing elit, sed do eiusmod tempor incididunt ut labore et dolore magna aliqua.</p>
<div class="feature" style="left:107px;top:1325px"><svg width="40" height="32"><rect x="10" y="10" width="14" height="14" transform="rotate(45 17 17)" fill="#f28b6b"/><rect x="20" y="12" width="12" height="12" transform="rotate(45 26 18)" fill="#4a5a7a"/><circle cx="20" cy="8" r="7" fill="var(--green)"/><path d="M16 8l3 3 5-5" stroke="#fff" stroke-width="2" fill="none"/></svg>100% reliable</div>
<div class="feature" style="left:270px;top:1325px"><svg width="40" height="34"><rect x="8" y="14" width="22" height="18" rx="5" fill="#f7a386"/><rect x="18" y="4" width="7" height="14" rx="3" fill="#f7a386"/><path d="M22 0v3M14 4l2 2M30 4l-2 2" stroke="#f4b13a" stroke-width="2"/></svg>Easy to use</div>
<div class="feature" style="left:433px;top:1325px"><svg width="44" height="30"><path d="M4 26 A18 18 0 0 1 40 26" fill="none" stroke="url(#gauge)" stroke-width="6"/><defs><linearGradient id="gauge"><stop offset="0" stop-color="#f4b13a"/><stop offset=".5" stop-color="#ea3a3a"/><stop offset="1" stop-color="#3b5be0"/></linearGradient></defs><path d="M22 26 L36 10" stroke="#3b8be0" stroke-width="4" stroke-linecap="round"/></svg>Performant</div>
<a class="btn" style="left:99px;top:1470px;width:181px;height:47px">More information</a>

<div class="panel" style="left:710px;top:1113px;width:322px;height:357px">
  <h4 style="padding:15px 16px;border-bottom:1px solid var(--line)">Session By Channel</h4>
  <svg class="abs" style="left:92px;top:70px" width="138" height="138" viewBox="0 0 138 138">
    <g fill="none" stroke-width="26">
      <path d="M69 13 A56 56 0 0 1 125 69" stroke="var(--pink)"/>
      <path d="M125 69 A56 56 0 0 1 100 116" stroke="var(--amber)"/>
      <path d="M100 116 A56 56 0 0 1 38 116" stroke="var(--teal)"/>
      <path d="M38 116 A56 56 0 0 1 69 13" stroke="var(--blue)"/>
    </g>
    <text x="69" y="70" text-anchor="middle" font-family="Poppins,sans-serif" font-size="16" font-weight="600" fill="#1f2a3d">82%</text>
    <text x="69" y="84" text-anchor="middle" font-family="Poppins,sans-serif" font-size="7" fill="#8a93a3">Reached</text>
  </svg>
  <div class="small abs" style="left:15px;top:256px;font-size:9px">ORGA</div>
  <div class="abs" style="left:15px;top:272px;font-size:11px;font-weight:600;color:var(--ink)"><span style="color:var(--amber)">●</span> 2,3</div>
  <div class="small abs" style="left:15px;top:305px;font-size:9px">REFFE</div>
  <div class="abs" style="left:15px;top:321px;font-size:11px;font-weight:600;color:var(--ink)"><span style="color:var(--blue)">●</span> 2,3</div>
</div>
<svg class="abs" style="left:1044px;top:1192px" width="50" height="180"><g fill="var(--teal)"><circle cx="3" cy="3" r="1.5"/><circle cx="24" cy="3" r="1.5"/><circle cx="45" cy="3" r="1.5"/><circle cx="3" cy="25" r="1.5"/><circle cx="24" cy="25" r="1.5"/><circle cx="45" cy="25" r="1.5"/><circle cx="3" cy="47" r="1.5"/><circle cx="24" cy="47" r="1.5"/><circle cx="45" cy="47" r="1.5"/><circle cx="3" cy="69" r="1.5"/><circle cx="24" cy="69" r="1.5"/><circle cx="45" cy="69" r="1.5"/><circle cx="3" cy="91" r="1.5"/><circle cx="24" cy="91" r="1.5"/><circle cx="45" cy="91" r="1.5"/><circle cx="45" cy="113" r="1.5"/><circle cx="45" cy="135" r="1.5"/><circle cx="45" cy="157" r="1.5"/><circle cx="45" cy="177" r="1.5"/></g></svg>
<div class="panel" style="left:756px;top:1302px;width:320px;height:250px;padding:18px 20px">
  <h4>Acquisition</h4>
  <p class="small" style="font-size:8.5px;line-height:11px;margin-top:8px">Tells you where your visitors originated from, such as search engines, social networks or website referrals.</p>
  <svg class="abs" style="left:20px;top:115px" width="278" height="118" viewBox="0 0 278 118">
    <path d="M0 18 L16 28 L30 22 L42 30 L60 30 L78 14 L94 14 L120 24 L150 22 L160 16 L176 30 L200 26 L218 18 L232 30 L250 34 L266 28 L278 30" fill="none" stroke="#a7acb8" stroke-width="1.2"/>
    <path d="M0 106 L14 94 L30 80 L42 84 L60 90 L70 84 L96 74 L120 60 L140 66 L154 70 L180 64 L206 54 L226 62 L238 70 L258 72 L272 70 L278 60 L278 118 L0 118Z" fill="#e6e9fb"/>
    <path d="M0 106 L14 94 L30 80 L42 84 L60 90 L70 84 L96 74 L120 60 L140 66 L154 70 L180 64 L206 54 L226 62 L238 70 L258 72 L272 70 L278 60" fill="none" stroke="var(--blue)" stroke-width="1.2"/>
  </svg>
</div>

<!-- Self-Service Terminals -->
<div class="panel" style="left:99px;top:1716px;width:322px;height:286px;padding:18px 16px">
  <h4>Agent Performance Points</h4>
  <div class="abs" role="img" aria-label="Agent profile picture" style="left:15px;top:56px;width:34px;height:34px;border-radius:50%;background:#c9b49d"></div>
  <div class="abs" style="left:58px;top:60px;font-size:9px;font-weight:600;color:var(--ink)">Lorem ipsum dolor</div>
  <div class="abs small" style="left:58px;top:74px;font-size:9px">Technical Support</div>
  <div class="abs" style="left:280px;top:62px;width:8px;height:8px;border-radius:50%;background:var(--blue)"></div>
  <div class="abs" style="left:58px;top:95px;width:230px;height:3px;background:#e4e7f2"><div style="width:85%;height:3px;background:var(--blue)"></div></div>
  <div class="abs" style="left:58px;top:104px;width:230px;display:flex;justify-content:space-between;font-size:9px;color:var(--ink)"><span>Executive Level</span><span>213,435,890</span></div>
  <div class="abs" role="img" aria-label="Agent profile picture" style="left:15px;top:128px;width:34px;height:34px;border-radius:50%;background:#e0a995"></div>
  <div class="abs" role="img" aria-label="Agent profile picture" style="left:15px;top:198px;width:34px;height:34px;border-radius:50%;background:#2a8aa0"></div>
</div>
<svg class="abs" style="left:431px;top:1756px" width="72" height="182"><g fill="var(--teal)"><circle cx="3" cy="3" r="1.5"/><circle cx="25" cy="3" r="1.5"/><circle cx="47" cy="3" r="1.5"/><circle cx="69" cy="3" r="1.5"/><circle cx="3" cy="25" r="1.5"/><circle cx="25" cy="25" r="1.5"/><circle cx="47" cy="25" r="1.5"/><circle cx="69" cy="25" r="1.5"/><circle cx="3" cy="47" r="1.5"/><circle cx="25" cy="47" r="1.5"/><circle cx="47" cy="47" r="1.5"/><circle cx="69" cy="47" r="1.5"/><circle cx="3" cy="69" r="1.5"/><circle cx="69" cy="69" r="1.5"/><circle cx="69" cy="91" r="1.5"/><circle cx="47" cy="113" r="1.5"/><circle cx="69" cy="113" r="1.5"/><circle cx="47" cy="135" r="1.5"/><circle cx="69" cy="135" r="1.5"/><circle cx="47" cy="157" r="1.5"/><circle cx="69" cy="157" r="1.5"/><circle cx="47" cy="179" r="1.5"/><circle cx="69" cy="179" r="1.5"/></g></svg>
<div class="panel" style="left:145px;top:1839px;width:322px;height:252px">
  <h4 style="padding:15px 16px;border-bottom:1px solid var(--line)">Device Session</h4>
  <div class="abs" style="left:16px;top:70px;display:flex;gap:28px;font-size:9px;color:var(--muted)">
    <div><span style="color:var(--blue)">●</span> MOBILE<div style="font-size:11px;font-weight:600;color:var(--ink);margin-top:6px;padding-left:16px">4,345</div></div>
    <div><span style="color:#e5745a">●</span> DESKTOP<div style="font-size:11px;font-weight:600;color:var(--ink);margin-top:6px;padding-left:16px">4,345</div></div>
    <div><span style="color:#d5d8df">●</span> OTHER<div style="font-size:11px;font-weight:600;color:var(--ink);margin-top:6px;padding-left:16px">4,345</div></div>
  </div>
  <svg class="abs" style="left:16px;top:112px" width="292" height="104" viewBox="0 0 292 104">
    <g stroke="#eceef3"><line x1="0" y1="0" x2="0" y2="104"/><line x1="36" y1="0" x2="36" y2="104"/><line x1="72" y1="0" x2="72" y2="104"/><line x1="108" y1="0" x2="108" y2="104"/><line x1="144" y1="0" x2="144" y2="104"/><line x1="180" y1="0" x2="180" y2="104"/><line x1="216" y1="0" x2="216" y2="104"/><line x1="252" y1="0" x2="252" y2="104"/><line x1="290" y1="0" x2="290" y2="104"/></g>
    <path d="M0 70 L20 84 L40 66 L70 76 L110 68 L130 30 L160 34 L190 42 L220 10 L240 28 L260 50 L280 40 L292 24 L292 104 L0 104Z" fill="#d7f4fa" opacity=".8"/>
    <path d="M0 70 L20 84 L40 66 L70 76 L110 68 L130 30 L160 34 L190 42 L220 10 L240 28 L260 50 L280 40 L292 24" fill="none" stroke="#8fe0ef" stroke-width="1.2"/>
    <path d="M0 88 L12 92 L24 84 L40 90 L70 90 L100 86 L130 76 L160 70 L186 74 L196 84 L210 74 L240 74 L260 80 L280 66 L292 64" fill="none" stroke="var(--blue)" stroke-width="1.5"/>
    <line x1="0" y1="103" x2="292" y2="103" stroke="#c9ccd4"/>
  </svg>
  <div class="abs small" style="left:10px;top:231px;width:306px;display:flex;justify-content:space-between;font-size:9.5px"><span>10</span><span>20</span><span>30</span><span>40</span><span>50</span><span>60</span><span>70</span><span>80</span><span>90</span></div>
</div>

<svg class="abs" style="left:613px;top:1714px" width="42" height="26"><path d="M2 6 L40 2 L24 12 L14 24 Z" fill="var(--accent)"/></svg>
<h3 class="abs prod-title" style="left:613px;top:1750px">Self-Service Terminals</h3>
<p class="abs prod-copy" style="left:613px;top:1810px;width:480px">Lorem ipsum dolor sit amet, consectetur adipiscing elit, sed do eiusmod tempor incididunt ut labore et dolore magna aliqua.</p>
<div class="feature soft" style="left:621px;top:1893px"><svg width="40" height="32"><rect x="10" y="10" width="14" height="14" transform="rotate(45 17 17)" fill="#f28b6b"/><rect x="20" y="12" width="12" height="12" transform="rotate(45 26 18)" fill="#4a5a7a"/><circle cx="20" cy="8" r="7" fill="var(--green)"/><path d="M16 8l3 3 5-5" stroke="#fff" stroke-width="2" fill="none"/></svg>100% reliable</div>
<div class="feature soft" style="left:784px;top:1893px"><svg width="40" height="34"><rect x="8" y="14" width="22" height="18" rx="5" fill="#f7a386"/><rect x="18" y="4" width="7" height="14" rx="3" fill="#f7a386"/><path d="M22 0v3M14 4l2 2M30 4l-2 2" stroke="#f4b13a" stroke-width="2"/></svg>Easy to use</div>
<div class="feature soft" style="left:947px;top:1893px"><svg width="44" height="30"><path d="M4 26 A18 18 0 0 1 40 26" fill="none" stroke="url(#gauge)" stroke-width="6"/><path d="M22 26 L36 10" stroke="#3b8be0" stroke-width="4" stroke-linecap="round"/></svg>Performant</div>
<a class="btn" style="left:613px;top:2045px;width:181px;height:47px">More information</a>

</body>
</html>
```